Bluestone Nine LLC Flyer Design

Marketing Materials for Real Estate Company. This flyer will be used to promote the company throughout the Commercial Real Estate business in the United States. The team has been together for 15 years. We are the middle guys between the Tenant, Broker, and the Owner. In the case of working with a Franchisor, we will be their Plug and Play leasing arm that will assist their new Franchisee's with their site selection, lease negotiations, design and construction management.

Target Market(s)

Real Estate Owners, Franchisor's, and Brokers

Font styles to use
Serif

Colors

Designer to choose colors to be used in the design.

Requirements
Must have
• The flyer must have......
• 1. The Best Leasing Machine On The Planet
• 2. Over the past 15 years our group has completed 4,492 lease transactions resulting in leasing 17,803,114 square feet in shopping centers across the United States.
• 3. Plug and Play Leasing Specialists. We handle the details between when the broker shows up with the space and the tenant and completing the lease negotiations, legal negotiations and documentation, and construction management to Certificate of Occupancy.
• 4. For Information Call Colette Varga at 555-014-2763 or Wendy Falk at 555-017-8302.
Nice to have
• National Tenants the we have completed transactions with....
• Pellmart, Fresh Basket, Harbor Pams, Vexo, Dunn, QV Rendo, Burrasco, Pattersons, Wrap Shack, Brewhorns, Summit Workout, ShipVo, Tredwell, PKN, Halvorsons, Q&L, Ledger Union Bank, Hen Haus-O, Lotus Kitchen, Furvo, Dex-Mart, Fieldly, and Orbit Theaters

```html
<!DOCTYPE html>
<html lang="en">
<head>
<meta charset="utf-8">
<title>Bluestone Nine LLC Flyer</title>
<link href="https://fonts.googleapis.com/css2?family=Roboto+Condensed:wght@300;400;700&family=Roboto:wght@300;700&display=swap" rel="stylesheet">
<style>
  :root{
    --navy:#171b27;
    --navy-deep:#0f121a;
    --green:#a6cb5b;
    --green-text:#a8cd5e;
    --ink:#1b1f16;
    --white:#ffffff;
    --page:#e9eaec;
  }
  *{box-sizing:border-box;margin:0;padding:0}
  html,body{width:1200px;height:1200px;overflow:hidden;background:var(--page)}
  .flyer{
    position:absolute;left:160px;top:30px;width:880px;height:1140px;
    background:var(--navy);color:var(--white);
    font-family:"Roboto Condensed",Arial,sans-serif;
    overflow:hidden;
  }
  .masthead{position:absolute;left:0;top:0;width:100%;height:153px;text-align:center}
  .brand-name{
    position:absolute;left:0;right:0;top:46px;
    font-family:"Roboto Condensed",Arial,sans-serif;font-weight:400;
    font-size:50px;letter-spacing:3px;color:var(--green-text);line-height:1;
  }
  .tagline{
    position:absolute;left:0;right:0;top:114px;
    font-family:"Roboto",Arial,sans-serif;font-weight:300;font-size:15.5px;color:var(--green-text);
  }
  .tagline b{font-weight:700}
  .hero-photo{
    position:absolute;left:0;top:153px;width:100%;height:518px;
    background:
      radial-gradient(ellipse at 25% 55%, #2a2d35 0%, rgba(42,45,53,0) 45%),
      radial-gradient(ellipse at 85% 60%, #1f2638 0%, rgba(31,38,56,0) 45%),
      linear-gradient(180deg,#dfe6ec 0%,#c7d1d8 45%,#8d969e 80%,#3a3f47 100%);
  }
  .hero-headline{position:absolute;left:68px;top:516px;line-height:1.12}
  .hero-headline .line{display:block;font-size:35px;font-weight:400;color:var(--white)}
  .hero-headline .line.accent{font-size:43px;color:var(--green-text)}
  .stats-band{
    position:absolute;left:0;top:671px;width:100%;height:83px;background:var(--green);
    color:var(--ink);text-align:center;font-size:19.5px;padding-top:9px;line-height:39px;
  }
  .stats-band strong{font-weight:700;font-size:24px}
  .column{position:absolute;top:790px}
  .column-left{left:68px;width:320px}
  .column-right{left:441px;width:380px}
  .column-divider{position:absolute;left:405px;top:795px;width:1px;height:222px;background:#3d4a2a}
  .section-title{font-size:27px;font-weight:400;color:var(--green-text);line-height:1.2}
  .section-title small{font-size:21px}
  .section-body{margin-top:18px;font-size:16px;font-weight:300;line-height:21px;color:var(--white)}
  .tenant-list{margin-top:16px;font-size:16.5px;font-weight:300;line-height:30.5px;color:var(--white)}
  .contact-bar{
    position:absolute;left:0;top:1057px;width:100%;height:83px;background:var(--navy-deep);
    text-align:center;font-size:21.5px;line-height:83px;color:var(--green-text);
  }
  .contact-bar b{font-weight:700}
</style>
</head>
<body>
  <main class="flyer">
    <header class="masthead">
      <div class="brand-name">Bluestone Nine LLC</div>
      <p class="tagline">We are the middle guys between the <b>Tenant, Broker</b>, and the <b>Owner.</b></p>
    </header>

    <div class="hero-photo" role="img" aria-label="Photo of business people in suits shaking hands across a meeting table in a bright office"></div>

    <h1 class="hero-headline">
      <span class="line">The Best</span>
      <span class="line accent">Leasing Machine</span>
      <span class="line">On The Planet</span>
    </h1>

    <p class="stats-band">
      Over the past <strong>15 years</strong> our group has completed <strong>4,492</strong> lease transactions resulting in leasing<br>
      <strong>17,803,114</strong> square feet in shopping centers across the United States.
    </p>

    <section class="column column-left">
      <h2 class="section-title">Plug and Play Leasing Specialists.</h2>
      <p class="section-body">We handle the details between when the broker shows up with the space and the tenant and completing the lease negotiations, legal negotiations and documentation, and construction management to Certificate of Occupancy.</p>
    </section>

    <div class="column-divider"></div>

    <section class="column column-right">
      <h2 class="section-title">National Tenants <small>the we have completed transactions with....</small></h2>
      <p class="tenant-list">Pellmart, Fresh Basket, Harbor Pams, Vexo, Dunn, QV Rendo, Burrasco, Pattersons, Wrap Shack, Brewhorns, Summit Workout, ShipVo, Tredwell, PKN, Halvorsons, Q&amp;L, Ledger Union Bank, Hen Haus-O, Lotus Kitchen, Furvo, Dex-Mart, Fieldly, and Orbit Theaters</p>
    </section>

    <footer class="contact-bar">
      For Information Call <b>Colette Varga at 555-014-2763</b> or <b>Wendy Falk at 555-017-8302.</b>
    </footer>
  </main>
</body>
</html>
```